Business Consulting Business Card

professional business card with basic information (1) First and Last name (2) email address, (3) phone number, (4) website.

```html
<!DOCTYPE html>
<html lang="en">
<head>
<meta charset="utf-8">
<title>Tidal Crest Business Card</title>
<link rel="stylesheet" href="https://fonts.googleapis.com/css2?family=Lato:wght@400;700&family=Montserrat:wght@500&display=swap">
<style>
  :root {
    --stage: #2a2a2c;
    --card: #0a2940;
    --card-deep: #08233a;
    --pattern: #16384f;
    --teal: #4bb8c9;
    --white: #f4f7f9;
    --rule: #2f6f86;
  }
  * { box-sizing: border-box; margin: 0; padding: 0; }
  html, body { width: 1200px; height: 1108px; overflow: hidden; }
  body {
    background: var(--stage);
    font-family: "Lato", sans-serif;
    position: relative;
  }
  .card {
    position: absolute;
    top: 224px;
    width: 380px;
    height: 660px;
    background: var(--card);
    border-radius: 22px;
    overflow: hidden;
  }
  .card--front { left: 170px; }
  .card--back { left: 650px; }

  .brand {
    position: absolute;
    top: 92px;
    left: 0;
    right: 0;
    display: flex;
    align-items: center;
    justify-content: center;
    gap: 16px;
  }
  .brand__dot {
    width: 40px; height: 40px;
    border-radius: 50%;
    background: var(--teal);
  }
  .brand__name {
    font-family: "Montserrat", sans-serif;
    font-weight: 500;
    font-size: 22px;
    letter-spacing: 7px;
    color: var(--white);
  }

  .person {
    position: absolute;
    top: 318px;
    left: 0; right: 0;
    text-align: center;
  }
  .person__name {
    font-weight: 700;
    font-size: 28px;
    color: var(--teal);
    letter-spacing: 0.5px;
  }
  .person__title {
    font-size: 18px;
    color: var(--white);
    margin-top: 4px;
  }

  .icon-rule {
    position: absolute;
    top: 392px;
    left: 60px; right: 60px;
    display: flex;
    align-items: center;
    gap: 6px;
  }
  .icon-rule__line { flex: 1; height: 1px; background: var(--rule); }
  .icon-rule svg { display: block; }

  .contact {
    position: absolute;
    top: 434px;
    left: 0; right: 0;
    text-align: center;
    color: var(--white);
    font-size: 18px;
    line-height: 29px;
  }
  .divider {
    position: absolute;
    top: 542px;
    left: 60px; right: 60px;
    height: 1px;
    background: var(--rule);
  }
  .address {
    position: absolute;
    top: 562px;
    left: 0; right: 0;
    text-align: center;
    color: var(--white);
    font-size: 18px;
    line-height: 28px;
  }

  .pattern-field {
    position: absolute;
    inset: 0 0 170px 0;
    background: linear-gradient(180deg, var(--pattern) 0%, var(--pattern) 60%, var(--card) 100%);
  }
  .back-mark {
    position: absolute;
    right: 44px;
    bottom: 120px;
    display: flex;
    align-items: center;
    gap: 12px;
  }
  .back-mark .brand__dot { width: 52px; height: 52px; }
  .back-mark__name {
    font-family: "Montserrat", sans-serif;
    font-weight: 500;
    font-size: 18px;
    letter-spacing: 5px;
    color: var(--white);
  }
</style>
</head>
<body>
  <section class="card card--front" aria-label="Card front">
    <div class="brand">
      <span class="brand__dot"></span>
      <span class="brand__name">TIDAL CREST</span>
    </div>

    <div class="person">
      <p class="person__name">DANIEL REYES</p>
      <p class="person__title">Founder | CEO</p>
    </div>

    <div class="icon-rule">
      <span class="icon-rule__line"></span>
      <svg width="84" height="26" viewBox="0 0 84 26" aria-hidden="true">
        <g fill="var(--teal)">
          <circle cx="13" cy="13" r="12"/>
          <circle cx="42" cy="13" r="12"/>
          <circle cx="71" cy="13" r="12"/>
        </g>
        <path d="M9 7c1-1 2-1 3 1l1 2c0 1-1 1-1 2 1 2 2 3 3 3 1 0 1-1 2-1l2 1c2 1 2 2 1 3-2 2-5 1-8-2s-5-6-3-9z" fill="var(--card)"/>
        <rect x="34" y="8" width="16" height="10" rx="1" fill="var(--card)"/>
        <path d="M34 8l8 6 8-6" stroke="var(--teal)" stroke-width="1.3" fill="none"/>
        <circle cx="71" cy="13" r="7" fill="none" stroke="var(--card)" stroke-width="1.5"/>
        <path d="M64 13h14M71 6v14M71 6c-4 4-4 10 0 14M71 6c4 4 4 10 0 14" stroke="var(--card)" stroke-width="1.2" fill="none"/>
      </svg>
      <span class="icon-rule__line"></span>
    </div>

    <div class="contact">
      <p>1234567890</p>
      <p>info@yourmail.com</p>
      <p>www.yourwebsite.com</p>
    </div>

    <div class="divider"></div>

    <div class="address">
      <p>1234 First Line Address</p>
      <p>5678 Second Line Address</p>
    </div>
  </section>

  <section class="card card--back" aria-label="Card back">
    <div class="pattern-field" role="img" aria-label="Faint repeating brand pattern fading toward the bottom"></div>
    <div class="back-mark">
      <span class="brand__dot"></span>
      <span class="back-mark__name">TIDAL CREST</span>
    </div>
  </section>
</body>
</html>
```